Logo for different Types of Exotic Salt

Dear Sirs, we are looking for a product logo for our 4 different types of Coral Salt. Colours Black/white/green and yellow.
Our Brand name is "Coral Breezers". It will be packed later in a small Tube size 100-150 Gramm. . We have already made a few designs (flowers and the black one with the tiki) so that you know roughly in which direction it should go. Attached also a picture of the packaging tube. On the backside there musst be the later the Ingrediens-we dont have them yet exactly. If you have any questions, please contact me at Brandt@lanternwaves.de Best regards Lukas Brandt
Target Market(s)
Zentrovo, Retail
Industry/Entity Type
Food
Colors
Designer to choose colors to be used in the design.
Requirements
Must have
- Association for Hawaii
Nice to have
- would be nice to ad "Premium Quality" Strong associaton with Hawaii

```html
<!DOCTYPE html>
<html lang="en">
<head>
<meta charset="utf-8">
<title>Coral Breezers – White Hawaii Salt Label</title>
<link href="https://fonts.googleapis.com/css2?family=Kaushan+Script&family=Marck+Script&family=Rubik:wght@500;700&display=swap" rel="stylesheet">
<style>
  :root {
    --stage: #dcd6c2;
    --ray-light: #a4a5a8;
    --ray-dark: #8c8d91;
    --panel: #545358;
    --frame: #ffffff;
    --paper: #ffffff;
    --ink: #161616;
    --petal: #f4f4f2;
    --leaf: #6f8f62;
  }
  html, body {
    margin: 0;
    padding: 0;
    width: 1200px;
    height: 842px;
    overflow: hidden;
    background: var(--stage);
  }
  .canvas {
    position: relative;
    width: 1200px;
    height: 842px;
  }
  .label {
    position: absolute;
    left: 355px;
    top: 53px;
    width: 490px;
    height: 736px;
    overflow: hidden;
    box-shadow: 3px 4px 6px rgba(0, 0, 0, 0.25);
  }
  .label-art {
    position: absolute;
    inset: 0;
    display: block;
  }
  .brand-script {
    position: absolute;
    left: 0;
    width: 490px;
    top: 215px;
    text-align: center;
    font-family: "Kaushan Script", cursive;
    font-size: 80px;
    line-height: 1;
    color: var(--frame);
  }
  .product-name {
    position: absolute;
    left: 0;
    width: 490px;
    top: 525px;
    text-align: center;
    font-family: "Marck Script", cursive;
    font-size: 70px;
    line-height: 1;
    color: var(--ink);
  }
  .product-type {
    position: absolute;
    left: 0;
    width: 490px;
    top: 604px;
    text-align: center;
    font-family: "Rubik", sans-serif;
    font-weight: 700;
    font-size: 29px;
    line-height: 1;
    color: var(--ink);
  }
  .quality-note {
    position: absolute;
    left: 0;
    width: 490px;
    top: 642px;
    text-align: center;
    font-family: "Rubik", sans-serif;
    font-weight: 500;
    font-size: 14px;
    line-height: 1;
    color: var(--ink);
  }
</style>
</head>
<body>
<main class="canvas">
  <section class="label">
    <svg class="label-art" viewBox="0 0 490 736" width="490" height="736" aria-hidden="false">
      <defs>
        <radialGradient id="ray-glow" cx="0.5" cy="0.42" r="0.75">
          <stop offset="0" stop-color="var(--ray-light)"/>
          <stop offset="1" stop-color="var(--ray-dark)"/>
        </radialGradient>
        <radialGradient id="bloom-tone" cx="0.55" cy="0.5" r="0.55">
          <stop offset="0" stop-color="var(--petal)"/>
          <stop offset="0.6" stop-color="#e6e6e3"/>
          <stop offset="1" stop-color="var(--leaf)"/>
        </radialGradient>
      </defs>
      <rect class="sunburst" x="0" y="0" width="490" height="736" fill="url(#ray-glow)" role="img" aria-label="Grey sunburst rays radiating from the label centre"/>
      <rect class="title-panel" x="55" y="158" width="379" height="370" fill="var(--panel)" stroke="var(--frame)" stroke-width="7"/>
      <ellipse class="bloom" cx="262" cy="410" rx="140" ry="90" fill="url(#bloom-tone)" role="img" aria-label="White hibiscus-style flower with green leaves"/>
      <path class="base-wave" d="M0 490 C 110 480, 190 515, 290 522 C 370 527, 430 492, 490 480 L 490 736 L 0 736 Z" fill="var(--paper)"/>
    </svg>
    <div class="brand-script">Coral</div>
    <div class="product-name">Breezers</div>
    <div class="product-type">WHITE HAWAII SALT</div>
    <div class="quality-note">PREMIUM QUALITY</div>
  </section>
</main>
</body>
</html>
```